Marlowe Creative Works Business Card Design

We need a double-sided business card for our company Marlowe Creative Works. Our slogan is "Simple Online Solutions." We are looking for a techy, cutting-edge but simple card that looks modern and sleek. We have a black logo attached and would prefer a lighter background to make our logo stand out. We like nice accents to make it pop out and make our clients remember our card.

On the back side, we just want our logo, slogan and website. Again, something very simple. Make the logo big on the back.

```html
<!DOCTYPE html>
<html lang="en">
<head>
<meta charset="utf-8">
<title>Marlowe Creative Works – Business Card</title>
<link rel="stylesheet" href="https://fonts.googleapis.com/css2?family=Questrial&family=Montserrat:wght@700&display=swap">
<style>
  :root {
    --page-bg: #ecebe8;
    --card-bg: #c8c8c8;
    --card-edge: #b4b4b4;
    --ink: #151515;
    --ink-soft: #3a3a3a;
    --rule: #4a4a4a;
  }
  * { box-sizing: border-box; margin: 0; padding: 0; }
  html, body { width: 1200px; height: 600px; overflow: hidden; }
  body {
    background: var(--page-bg);
    font-family: "Questrial", "Century Gothic", sans-serif;
    color: var(--ink);
    position: relative;
  }
  .card {
    position: absolute;
    top: 145px;
    width: 540px;
    height: 310px;
    background: var(--card-bg);
    border: 1px solid var(--card-edge);
    box-shadow: 0 6px 18px rgba(0,0,0,0.18);
  }
  .card--back { left: 30px; }
  .card--front { left: 630px; }

  .wordmark {
    font-family: "Questrial", "Century Gothic", sans-serif;
    color: var(--ink);
    white-space: nowrap;
    letter-spacing: -0.5px;
  }

  /* Back side: large logo, website, rule, slogan */
  .card--back .wordmark {
    position: absolute;
    right: 34px;
    top: 62px;
    font-size: 40px;
  }
  .card--back .website {
    position: absolute;
    right: 36px;
    top: 116px;
    font-family: "Montserrat", sans-serif;
    font-weight: 700;
    font-size: 14px;
    letter-spacing: 0.3px;
  }
  .card--back .divider {
    position: absolute;
    left: 34px;
    right: 34px;
    top: 152px;
    height: 1px;
    background: var(--rule);
  }
  .card--back .slogan {
    position: absolute;
    left: 40px;
    top: 170px;
    font-size: 15px;
    letter-spacing: 3px;
    color: var(--ink-soft);
  }

  /* Front side: contact block and logo */
  .card--front .wordmark {
    position: absolute;
    right: 28px;
    top: 78px;
    font-size: 23px;
  }
  .person {
    position: absolute;
    left: 30px;
    top: 86px;
  }
  .person__name {
    font-family: "Montserrat", sans-serif;
    font-weight: 700;
    font-size: 17px;
  }
  .person__title {
    font-size: 13px;
    color: var(--ink-soft);
    margin-top: 1px;
  }
  .contact-list {
    position: absolute;
    left: 30px;
    top: 136px;
    list-style: none;
  }
  .contact-list li {
    display: flex;
    align-items: center;
    gap: 9px;
    font-size: 13px;
    line-height: 20px;
    color: var(--ink-soft);
  }
  .contact-list svg { width: 11px; height: 11px; flex: none; fill: var(--ink); }
</style>
</head>
<body>

  <section class="card card--back" aria-label="Card back">
    <div class="wordmark">Marlowe Creative Works</div>
    <div class="website">www.marlowecreativeworks.com</div>
    <div class="divider"></div>
    <div class="slogan">Simple Online Solutions</div>
  </section>

  <section class="card card--front" aria-label="Card front">
    <div class="person">
      <div class="person__name">Daniel Ashford</div>
      <div class="person__title">Executive Director</div>
    </div>
    <ul class="contact-list">
      <li>
        <svg viewBox="0 0 12 12" aria-hidden="true"><path d="M3 0h6a1 1 0 0 1 1 1v10a1 1 0 0 1-1 1H3a1 1 0 0 1-1-1V1a1 1 0 0 1 1-1zm0 1.5v8h6v-8z"/></svg>
        +61 400 555 012
      </li>
      <li>
        <svg viewBox="0 0 12 12" aria-hidden="true"><path d="M1 3.5C1 2 2.5 1 6 1s5 1 5 2.5V5H8.5V4h-5v1H1zM2 6h8l1 5H1z"/></svg>
        +61 3 9000 1234
      </li>
      <li>
        <svg viewBox="0 0 12 12" aria-hidden="true"><path d="M0 2h12v8H0zm1.2 1 4.8 3.6L10.8 3z"/></svg>
        info@marlowecreativeworks.com
      </li>
      <li>
        <svg viewBox="0 0 12 12" aria-hidden="true"><path d="M6 0a6 6 0 1 0 0 12A6 6 0 0 0 6 0zm0 1.2c.7.7 1.2 2 1.4 3.6H4.6C4.8 3.2 5.3 1.9 6 1.2zM1.3 6.6h2.1c.1 1.4.5 2.7 1 3.6a4.8 4.8 0 0 1-3.1-3.6zm0-1.2a4.8 4.8 0 0 1 3.1-3.6c-.5.9-.9 2.2-1 3.6zm3.3 1.2h2.8C7.2 8.2 6.7 9.6 6 10.5c-.7-.9-1.2-2.3-1.4-3.9zm3-4.8a4.8 4.8 0 0 1 3.1 3.6H8.6c-.1-1.4-.5-2.7-1-3.6zm1 4.8h2.1a4.8 4.8 0 0 1-3.1 3.6c.5-.9.9-2.2 1-3.6z"/></svg>
        www.marlowecreativeworks.com
      </li>
      <li>
        <svg viewBox="0 0 12 12" aria-hidden="true"><path d="M6 0a4 4 0 0 1 4 4c0 3-4 8-4 8S2 7 2 4a4 4 0 0 1 4-4zm0 2.4a1.6 1.6 0 1 0 0 3.2 1.6 1.6 0 0 0 0-3.2z"/></svg>
        14 Example Lane Northvale VIC 3000
      </li>
    </ul>
    <div class="wordmark">Marlowe Creative Works</div>
  </section>

</body>
</html>
```